Logo and website for K-12 Academy- Lumora Crest Academy

Overview
Lumora Crest Academy is a new online educational institution based in Ghana & Portugal, offering a K-12 curriculum designed to empower the next generation with academic excellence, leadership skills, and deep-rooted cultural values. The academy emphasizes knowledge, mentorship, leadership, and a strong connection to African heritage.

Objective
Create a meaningful, timeless, and visually compelling logo that:

Represents growth, wisdom, and resilience through the imagery of the Odum Tree.

Symbolizes knowledge and academic pursuit.

Reflects mentorship and leadership development.

Appeals to parents and students alike, exuding trust, strength, and inspiration.

Key Themes
Odum Tree: A powerful symbol in Ghana, representing strength, endurance, and wisdom.

Knowledge: Books, light, open pathways, or abstract symbols of learning.

Mentorship/Leadership: Hands guiding others, rising figures, light leading the way, or interconnected branches.

Ghanaian Heritage: Subtle inclusion of Ghanaian cultural elements (such as color palette or patterns) without overwhelming the global, professional appeal.

Target Audience
Parents and guardians seeking quality education steeped in both academic rigor and cultural values.
Students from kindergarten through high school (ages 4–18).
Stakeholders and partners supporting education initiatives in Africa.

Style & Tone
Professional and Inspirational: Serious but welcoming.
Modern with Cultural Depth: Clean lines, minimal clutter, but with depth and meaning.
Warm and Trustworthy: The logo should evoke feelings of safety, hope, growth, and pride.
Flexible: It should work well in both full-color and monochrome versions, and look good at both large and small scales. Except for color changes and cultural elements, main logo should be able to be adapted to both countries
Color Palette (Suggestions)
Earth tones: Browns, greens — representing the Odum tree and growth
Gold/Yellow: For wisdom, enlightenment, and a nod to Ghana’s national colors.
Deep Red or Burgundy: Representing strength and heritage.
Logo Elements
Tree: Odum tree as the main, central symbol. Book, Light, or Path: Sub-elements to subtly symbolize knowledge and learning.
Mentorship: Perhaps visualized through multiple branches, a larger tree protecting smaller saplings, or guiding light themes.

Deliverables
Primary logo (full-color)
Secondary logo (single-color or black/white version)
Icon or emblem version (simplified for small applications like favicons or social media)
Logo usage guidelines (optional but preferred)

Target Market(s)

K-12 parents

Industry/Entity Type

Education

Coding

Coded - Design and coding required

Number of Pages Required

1 page

Font styles to use
Sans Serif

Requirements
Nice to have
• Inspirations Cultural motifs reimagined in a sleek, contemporary style. Nature-inspired logos that convey growth and resilience.

```html
<!DOCTYPE html>
<html lang="en">
<head>
<meta charset="utf-8">
<title>Lumora Crest Academy</title>
<link href="https://fonts.googleapis.com/css2?family=Bungee&family=Oswald:wght@300;400;500&display=swap" rel="stylesheet">
<style>
:root{
  --sand:#ecd3a4;
  --cream:#f1e3bd;
  --clay:#a84b3a;
  --ink:#2a2421;
  --olive:#7b8550;
  --gold:#e2b021;
  --paper:#fbf3df;
}
*{box-sizing:border-box;margin:0;padding:0}
html,body{width:1200px;height:3665px;overflow:hidden}
body{font-family:"Oswald",sans-serif;font-weight:300;color:var(--ink);background:var(--sand);position:relative}
.abs{position:absolute}
.display{font-family:"Bungee",sans-serif;font-weight:400;letter-spacing:1px}
.accent{color:var(--clay)}
.btn{position:absolute;display:flex;align-items:center;justify-content:center;border-radius:26px;color:#fff;font-size:17px;font-weight:400;height:50px}
.btn-clay{background:var(--clay)}
.btn-olive{background:var(--olive)}
.btn-outline{border:1.5px solid #f4dfd0;color:#fff}

/* header */
.brand{left:142px;top:60px;width:210px;display:flex;flex-direction:column;align-items:center;gap:12px;font-size:19px;font-weight:400;text-align:center}
.brand-dot{width:110px;height:110px;border-radius:50%;background:var(--olive)}
.nav{left:455px;top:60px;width:745px;height:48px;background:var(--ink);border-radius:24px 0 0 24px;display:flex;align-items:center;color:#fff;font-size:16px;font-weight:400}
.nav a{color:#fff;text-decoration:none;margin-right:27px}
.nav .active{background:var(--clay);height:48px;width:88px;border-radius:24px;display:flex;align-items:center;justify-content:center;margin-right:24px}

.hero-title{left:145px;top:278px;font-size:33px;line-height:45px}
.hero-sub{left:145px;top:423px;width:380px;font-size:17px;line-height:30px;font-weight:400}
.phone-ic{width:32px;height:32px;border-radius:50%;background:#fff;display:flex;align-items:center;justify-content:center;margin-right:10px}
.dots{left:145px;top:625px;display:flex;gap:14px}
.dots span{width:5px;height:5px;border-radius:50%;background:var(--ink)}
.dots span.on{background:var(--clay)}

/* about */
.tree-art{left:60px;top:760px;width:440px;height:580px;border-radius:45% 45% 20% 20%;background:radial-gradient(ellipse at 50% 30%,#b96b3e 0%,#7c6a3c 40%,rgba(42,36,33,.55) 70%,rgba(236,211,164,0) 90%)}
.bubble{position:absolute;border-radius:50%;display:flex;align-items:center;justify-content:center;text-align:center;color:#fff;font-size:11px;font-weight:500;line-height:15px;border:2px solid var(--sand)}
.sec-title{font-size:34px;line-height:40px}
.para{font-size:15.5px;line-height:28.3px;text-align:justify}

/* mentorship */
.band-cream{left:0;top:1395px;width:1200px;height:1600px;background:var(--cream)}
.card{position:absolute;top:1559px;width:290px;height:348px;overflow:hidden;color:#fff}
.card-photo{height:181px}
.card-body{padding:22px 31px 0;height:167px}
.card h3{font-size:16px;font-weight:400;margin-bottom:9px}
.card p{font-size:12.5px;line-height:21px}
.card .more{display:inline-block;margin-top:6px;font-size:12.5px;font-weight:500;text-decoration:underline}
.card-shadow{left:230px;top:1905px;width:740px;height:40px;border-radius:50%;background:radial-gradient(ellipse,rgba(42,36,33,.25),rgba(42,36,33,0) 70%)}

/* video */
.video{left:142px;top:2574px;width:914px;height:491px;border-radius:85px 0 0 0;border:2px solid #e8dcae;background:linear-gradient(110deg,#5d6d78 0%,#b9c3c6 35%,#8d6547 60%,#e0b541 100%);z-index:2}
.play{left:571px;top:2791px;width:58px;height:58px;border-radius:50%;background:var(--olive);border:2px solid #fff;display:flex;align-items:center;justify-content:center;z-index:3}
.band-clay{left:0;top:2971px;width:1200px;height:390px;background:var(--clay)}
.join{left:0;top:3112px;width:1200px;text-align:center;color:#fff;font-size:32px;line-height:45px}

/* footer */
.footer{left:0;top:3360px;width:1200px;height:305px;background:var(--cream)}
.footer-brand{left:171px;top:3400px;width:230px;display:flex;flex-direction:column;align-items:center;gap:12px;font-size:17px;font-weight:400}
.footer-nav{left:505px;top:3437px;display:flex;gap:25px;font-size:15px;font-weight:400}
.copy{left:505px;top:3483px;font-size:13px}
.socials{left:506px;top:3535px;display:flex;gap:10px}
.socials span{width:42px;height:42px;border-radius:50%;background:var(--ink)}
.socials span.alt{background:transparent;border:3px solid #2f6a2f}
</style>
</head>
<body>

<!-- header -->
<div class="abs brand"><div class="brand-dot"></div>Lumora Crest Academy</div>
<nav class="abs nav">
  <a class="active">Home</a><a>About Us</a><a>Academics</a><a>Mentorship</a><a>Admissions</a><a>News</a><a>Contact Us</a>
</nav>

<!-- hero -->
<h1 class="abs display hero-title">Empowering the<br><span class="accent">future,honoring</span><br>our heritage</h1>
<p class="abs hero-sub">Lumora Crest Academy blends global academic excellence with African cultural pride.</p>
<div class="btn btn-clay" style="left:145px;top:521px;width:155px">APPLY NOW</div>
<div class="btn btn-olive" style="left:313px;top:521px;width:192px">
  <span class="phone-ic"><svg width="18" height="18" viewBox="0 0 24 24"><path fill="#7b8550" d="M6.6 10.8a15 15 0 0 0 6.6 6.6l2.2-2.2c.3-.3.7-.4 1-.2 1.1.4 2.3.6 3.6.6.6 0 1 .4 1 1V20c0 .6-.4 1-1 1A17 17 0 0 1 3 4c0-.6.4-1 1-1h3.5c.6 0 1 .4 1 1 0 1.3.2 2.5.6 3.6.1.3 0 .7-.2 1z"/></svg></span>+1 555 014 2290
</div>
<div class="abs dots"><span></span><span></span><span></span><span class="on"></span></div>

<svg class="abs" style="left:570px;top:118px" width="590" height="622" viewBox="0 0 590 622" role="img" aria-label="Photo of a young girl with headphones writing at a desk">
  <defs><linearGradient id="heroFill" x1="0" y1="0" x2="1" y2="1"><stop offset="0" stop-color="#c9bba8"/><stop offset=".5" stop-color="#efe8df"/><stop offset="1" stop-color="#8a6a4e"/></linearGradient></defs>
  <path d="M170 30 C230 0 320 0 360 40 C420 20 500 60 510 130 C575 170 580 260 545 310 C585 370 560 460 500 480 C480 560 400 600 330 575 C270 615 190 600 160 545 C90 560 30 510 40 440 C0 400 5 320 55 290 C30 230 60 170 120 160 C120 100 140 50 170 30 Z" fill="url(#heroFill)" stroke="#2a2421" stroke-width="12"/>
</svg>

<!-- about -->
<div class="abs tree-art" role="img" aria-label="Illustration of a tree with an open book and children among its branches"></div>
<div class="bubble" style="left:134px;top:757px;width:68px;height:68px;background:var(--ink)">Leadership</div>
<div class="bubble" style="left:300px;top:739px;width:70px;height:70px;background:var(--olive)">Strong<br>connection</div>
<div class="bubble" style="left:38px;top:870px;width:70px;height:70px;background:var(--gold)">Mentorship</div>
<div class="bubble" style="left:183px;top:1020px;width:68px;height:68px;background:var(--clay)">Knowledge</div>

<h2 class="abs display sec-title" style="left:584px;top:872px">About <span class="accent">Us</span></h2>
<p class="abs para" style="left:584px;top:929px;width:464px">Sed ut perspiciatis unde omnis iste natus error sit voluptatem accusantium doloremque laudantium, totam rem aperiam, eaque ipsa quae ab illo inventore veritatis et quasi architecto beatae vitae dicta sunt explicabo. Nemo enim ipsam voluptatem quia voluptas sit aspernatur aut odit aut fugit, sed quia consequuntur magni dolores eos qui ratione voluptatem sequi nesciunt. Neque porro quisquam est, qui dolorem ipsum quia dolor sit amet, consectetur, adipisci velit, sed quia non numquam eius modi tempora incidunt ut labore et dolore magnam aliquam quaerat voluptatem</p>
<div class="btn btn-clay" style="left:584px;top:1160px;width:156px">LEARN MORE</div>
<div class="btn btn-olive" style="left:752px;top:1160px;width:155px">APPLY NOW</div>

<!-- mentorship -->
<div class="abs band-cream"></div>
<svg class="abs" style="left:0;top:1365px" width="1200" height="40" viewBox="0 0 1200 40" preserveAspectRatio="none"><path d="M0 30 L60 24 L120 32 L200 20 L260 28 L340 18 L420 30 L500 22 L580 30 L660 14 L740 26 L820 20 L900 8 L960 22 L1040 12 L1120 24 L1200 18 L1200 40 L0 40 Z" fill="#f1e3bd"/></svg>

<h2 class="abs display sec-title" style="left:0;top:1475px;width:1200px;text-align:center">Mentorship</h2>

<div class="card" style="left:144px;border-radius:70px 0 0 0;background:var(--clay)">
  <div class="card-photo" role="img" aria-label="Photo of a mentor helping a boy at a laptop" style="background:linear-gradient(120deg,#6c5a4b,#c9b8a2 50%,#3d4f70)"></div>
  <div class="card-body"><h3>HANDS GUIDING OTHERS</h3><p>Sed ut perspiciatis unde omnis iste natus error sit voluptatem accusantium doloremque laudantium, totam rem aperiam,</p><span class="more">READ MORE</span></div>
</div>
<div class="card" style="left:455px;border-radius:70px 0 0 0;background:var(--gold);border:2px solid #d79c12">
  <div class="card-photo" role="img" aria-label="Photo of a child using a tablet in a classroom" style="background:linear-gradient(120deg,#7e6a4f,#c9a46a 50%,#b9bfa6)"></div>
  <div class="card-body"><h3>RISING FIGURES</h3><p>Sed ut perspiciatis unde omnis iste natus error sit voluptatem accusantium doloremque laudantium, totam rem aperiam,</p><span class="more">READ MORE</span></div>
</div>
<div class="card" style="left:766px;border-radius:70px 0 0 0;background:var(--olive)">
  <div class="card-photo" role="img" aria-label="Photo of a student with headphones working on a laptop" style="background:linear-gradient(120deg,#5b7a86,#b98a66 50%,#a4302c)"></div>
  <div class="card-body"><h3>LIGHT LEADING THE WAY</h3><p>Sed ut perspiciatis unde omnis iste natus error sit voluptatem accusantium doloremque laudantium, totam rem aperiam,</p><span class="more">READ MORE</span></div>
</div>
<div class="abs card-shadow"></div>

<!-- cultural studies -->
<h2 class="abs display sec-title" style="left:145px;top:2128px">Cultural <span class="accent">Studies</span></h2>
<p class="abs para" style="left:145px;top:2185px;width:464px">Sed ut perspiciatis unde omnis iste natus error sit voluptatem accusantium doloremque laudantium, totam rem aperiam, eaque ipsa quae ab illo inventore veritatis et quasi architecto beatae vitae dicta sunt explicabo. Nemo enim ipsam voluptatem quia voluptas sit aspernatur aut odit aut fugit, sed quia consequuntur magni dolores eos qui ratione voluptatem sequi nesciunt. Neque porro quisquam est, qui dolorem ipsum quia dolor sit amet, consectetur, adipisci velit, sed quia non numquam eius modi tempora incidunt ut labore et dolore magnam aliquam quaerat voluptatem</p>
<div class="btn btn-clay" style="left:145px;top:2416px;width:157px">LEARN MORE</div>

<svg class="abs" style="left:662px;top:2008px" width="474" height="516" viewBox="0 0 474 516" role="img" aria-label="Photo of two smiling children celebrating with a flag">
  <defs><linearGradient id="cultFill" x1="0" y1="0" x2="1" y2="1"><stop offset="0" stop-color="#8c8478"/><stop offset=".45" stop-color="#6b4a35"/><stop offset=".8" stop-color="#3c8a55"/><stop offset="1" stop-color="#c9432f"/></linearGradient></defs>
  <path d="M150 60 C170 15 240 0 290 20 C340 5 410 40 420 100 C470 140 470 220 440 260 C470 320 450 400 390 420 C370 490 290 515 230 490 C170 515 100 490 80 440 C20 430 0 360 30 320 C0 270 20 200 70 185 C60 130 100 75 150 60 Z" fill="url(#cultFill)" stroke="#2a2421" stroke-width="12"/>
</svg>

<!-- video / join -->
<div class="abs band-clay"></div>
<div class="abs video" role="img" aria-label="Video still of a smiling girl waving at a laptop"></div>
<div class="abs play"><svg width="22" height="22" viewBox="0 0 24 24"><path d="M7 4 L20 12 L7 20 Z" fill="#fff"/></svg></div>
<h2 class="abs display join">Join a community where knowledge<br>and leadership grow hand in hand.</h2>
<div class="btn btn-olive" style="left:438px;top:3234px;width:156px">APPLY NOW</div>
<div class="btn btn-outline" style="left:606px;top:3234px;width:154px">LEARN MORE</div>

<!-- footer -->
<div class="abs footer"></div>
<svg class="abs" style="left:0;top:3320px" width="1200" height="42" viewBox="0 0 1200 42" preserveAspectRatio="none"><path d="M0 40 L100 36 L220 38 L360 34 L500 38 L640 30 L760 26 L860 20 L940 22 L1000 10 L1060 16 L1120 4 L1200 8 L1200 42 L0 42 Z" fill="#f1e3bd"/></svg>
<div class="abs footer-brand"><div class="brand-dot" style="width:120px;height:120px"></div>Lumora Crest Academy</div>
<div class="abs footer-nav"><span>Home</span><span>About Us</span><span>Academics</span><span>Mentorship</span><span>Admissions</span><span>News</span><span>Contact Us</span></div>
<p class="abs copy">© 2025 Companyname.All Rights Reserved &nbsp;|&nbsp; Privacy Policy &nbsp;|&nbsp; Terms of Use</p>
<div class="abs socials"><span></span><span></span><span class="alt"></span></div>

</body>
</html>
```